MARCO DELUCE FOR CONGRESS DISTRICT 32

I need to create a campaign flyer for my congress campaign. I am running for congress in District 32 of Texas as a civitist. I am a former Solvanic athlete, world champion fencer, Army veteran, Counterintelligence officer (I catch spies).
I want just my first name MARCO in big letters at the top. I want it to say MARCO and below it Civitist for Congress.
www.marcoforhouse.net

Political

EB3D1F
EC4F4E
F09395
F8D3D4
FCEDEE

• Would love a catchy title for the Flyer like "Spy Catcher", "Solvanic Athlete" "World Champion Fencer" running for Congress in your District!

```html
<!DOCTYPE html>
<html lang="en">
<head>
<meta charset="UTF-8">
<title>Marco Deluce for Congress – Flyer</title>
<link rel="stylesheet" href="https://fonts.googleapis.com/css2?family=Anton&family=Montserrat:wght@500;800;900&display=swap">
<style>
  :root {
    --red: #EB3D1F;
    --coral: #EC4F4E;
    --rose: #F09395;
    --blush: #F8D3D4;
    --mist: #FCEDEE;
    --navy: #2A3574;
    --white: #FFFFFF;
  }
  * { box-sizing: border-box; margin: 0; padding: 0; }
  html, body { width: 987px; height: 1200px; overflow: hidden; }
  body { background: var(--mist); position: relative; }

  .flyer {
    position: absolute; left: 29px; top: 0;
    width: 928px; height: 1200px; overflow: hidden;
    background: linear-gradient(180deg, var(--blush) 0%, #F5C2C3 45%, var(--rose) 100%);
  }
  .flyer__glow {
    position: absolute; left: 0; right: 0; top: 112px; height: 190px;
    background: radial-gradient(ellipse 60% 70% at 50% 50%, rgba(255,255,255,.95), rgba(255,255,255,.7) 60%, rgba(255,255,255,0) 100%);
  }
  .flyer__glow--top {
    top: 30px; height: 110px;
    background: radial-gradient(ellipse 30% 60% at 50% 50%, rgba(255,255,255,.85), rgba(255,255,255,0));
  }

  .brand {
    position: absolute; top: 66px; left: 0; right: 0;
    display: flex; justify-content: center; align-items: center; gap: 10px;
  }
  .brand__name {
    font-family: "Montserrat", sans-serif; font-weight: 900;
    font-size: 27px; color: var(--red); letter-spacing: .5px;
  }
  .brand__mark { width: 18px; height: 18px; background: var(--navy); }

  .headline {
    position: absolute; left: 0; right: 0; text-align: center;
    font-family: "Anton", sans-serif; color: var(--navy); text-transform: uppercase;
  }
  .headline--intro { top: 128px; font-size: 29px; letter-spacing: .2px; }
  .headline--intro .accent { color: #D4332A; }
  .headline--credentials { top: 186px; font-size: 40px; line-height: 50px; }

  .name-title {
    position: absolute; left: 64px; top: 396px;
    font-family: "Montserrat", sans-serif; font-weight: 900;
    font-size: 92px; line-height: 1; letter-spacing: -1px;
    color: var(--red);
    text-shadow:
      1px 0 0 var(--navy), -1px 0 0 var(--navy),
      0 1px 0 var(--navy), 0 -1px 0 var(--navy),
      2px 2px 0 var(--navy), 3px 3px 0 var(--navy), 4px 4px 0 var(--navy),
      5px 8px 10px rgba(42,53,116,.35);
    z-index: 3;
  }

  .party-line {
    position: absolute; left: 94px; width: 300px; top: 578px;
    text-align: center;
    font-family: "Anton", sans-serif; font-size: 62px; line-height: 68px;
    color: var(--navy); text-transform: uppercase;
    text-shadow: 2px 3px 4px rgba(42,53,116,.35);
  }

  .portrait {
    position: absolute; left: 444px; top: 312px; width: 520px; height: 900px;
    border-radius: 200px 190px 0 0;
    background: linear-gradient(180deg, #4A3A32 0%, #5B463C 9%, #E2B7A4 14%, #D8A894 45%, #E9E6EA 60%, #F7F7F9 100%);
    z-index: 2;
  }

  .badge {
    position: absolute; top: 821px; width: 216px; height: 216px;
    border-radius: 50%; border: 7px solid var(--red);
    box-shadow: 0 0 0 3px var(--white), 0 6px 14px rgba(0,0,0,.25);
    z-index: 4;
  }
  .badge--service { left: 65px; background: linear-gradient(160deg, #6B7483 0%, #7A7A5C 55%, #5E6249 100%); }
  .badge--fencing { left: 299px; background: linear-gradient(120deg, #E9E6E4 0%, #D9D4D0 45%, #D98A2B 100%); }

  .web-link {
    position: absolute; left: 61px; top: 1062px; width: 560px; height: 75px;
    border-radius: 40px; background: var(--white); padding: 8px;
    z-index: 1;
  }
  .web-link__bar {
    height: 100%; border-radius: 32px; background: var(--red);
    display: flex; align-items: center; padding-left: 18px; gap: 18px;
    font-family: "Montserrat", sans-serif; font-weight: 500;
    font-size: 21px; color: var(--white);
  }
  .web-link__icon { width: 24px; height: 24px; }
</style>
</head>
<body>
  <main class="flyer">
    <div class="flyer__glow flyer__glow--top"></div>
    <div class="flyer__glow"></div>

    <header class="brand">
      <span class="brand__name">MARCO DELUCE</span>
      <span class="brand__mark"></span>
    </header>

    <p class="headline headline--intro"><span class="accent">Running for Congress</span> in District 32 of Texas as a Civitist</p>
    <h2 class="headline headline--credentials">Solvanic Athlete, World Champion Fencer,<br>Army Veteran, Counterintelligence Officer</h2>

    <div class="portrait" role="img" aria-label="Portrait photo of the candidate in a white patterned shirt"></div>

    <h1 class="name-title">MARCO</h1>

    <p class="party-line">Civitist<br>for<br>Congress</p>

    <div class="badge badge--service" role="img" aria-label="Photo of the candidate in Army uniform"></div>
    <div class="badge badge--fencing" role="img" aria-label="Photo of the candidate fencing in competition"></div>

    <div class="web-link">
      <div class="web-link__bar">
        <svg class="web-link__icon" viewBox="0 0 24 24" fill="none" stroke="#FFFFFF" stroke-width="1.6">
          <circle cx="12" cy="12" r="10"/>
          <ellipse cx="12" cy="12" rx="4.5" ry="10"/>
          <line x1="2" y1="12" x2="22" y2="12"/>
          <path d="M4 6.5h16M4 17.5h16"/>
        </svg>
        <span>www.marcoforhouse.net</span>
      </div>
    </div>
  </main>
</body>
</html>
```